Business cards, stationary, envelopes and fax cover sheet
for Tessaline Goods
Simple
Corin Maddox
Founder, VP Operations and Marketing
P.O. Box 4682
Wildomar, CA 92871
corin@tessalinegoods.example
www.tessalinegoods.example
the logo on the backside
Business Logo
Business Symbol
Company name alone
logo in ai format
symbol in ai format
company name alone in ai format

```html
<!DOCTYPE html>
<html lang="en">
<head>
<meta charset="utf-8">
<title>Tessaline Goods — Stationery Set</title>
<link href="https://fonts.googleapis.com/css2?family=Open+Sans:wght@400;700&display=swap" rel="stylesheet">
<style>
  :root{
    --bg:#2b2d30;
    --paper:#ffffff;
    --green:#2f9e4c;
    --green-dark:#1f7a36;
    --blue:#1d5ea8;
    --navy:#1b2a3a;
    --ink:#444a50;
    --faint:#e9eef0;
    --rule:#c9ced2;
  }
  *{box-sizing:border-box;margin:0;padding:0}
  html,body{width:1200px;height:313px;overflow:hidden;background:var(--bg)}
  body{position:relative;font-family:"Open Sans",Arial,sans-serif;color:var(--ink)}
  .piece{position:absolute;background:var(--paper);overflow:hidden;box-shadow:0 2px 6px rgba(0,0,0,.35)}
  .brand{display:flex;align-items:center;gap:4px;font-weight:700;color:var(--green);white-space:nowrap}
  .brand .dot{border-radius:50%;background:var(--green);flex:none}
  .wave{position:absolute;left:0;bottom:0;width:100%}
  .tiny{font-size:4px;line-height:6px;color:var(--ink)}

  /* master logo */
  .logo-master{position:absolute;left:12px;top:24px;width:120px;text-align:center}
  .logo-master .brand{justify-content:center;font-size:16px}
  .logo-master .brand .dot{width:14px;height:14px}
  .logo-master .sub{font-size:6px;color:#cfd5d9;margin-top:3px}

  /* business cards */
  .card-dark{left:12px;top:108px;width:120px;height:70px;background:var(--navy)}
  .card-dark .brand{position:absolute;left:10px;top:28px;font-size:10px;color:#fff}
  .card-dark .brand .dot{width:8px;height:8px;background:#fff}
  .card-dark .wave{height:14px}
  .card-front{left:12px;top:211px;width:108px;height:60px}
  .card-front .brand{position:absolute;left:6px;top:8px;font-size:7px}
  .card-front .brand .dot{width:6px;height:6px}
  .card-front .details{position:absolute;right:6px;top:9px;text-align:right}
  .card-front .wave{height:12px}
  .card-back{left:132px;top:211px;width:108px;height:60px;background:var(--green)}
  .card-back .brand{position:absolute;left:0;right:0;top:24px;justify-content:center;font-size:9px;color:#fff}
  .card-back .brand .dot{width:7px;height:7px;background:#fff}

  /* letterhead & fax */
  .sheet{top:19px;width:200px;height:258px}
  .letterhead{left:264px}
  .fax{left:485px}
  .sheet .head{position:absolute;left:10px;top:10px}
  .sheet .head .brand{font-size:8px}
  .sheet .head .brand .dot{width:7px;height:7px}
  .sheet .contact{position:absolute;right:10px;top:10px;text-align:right}
  .sheet .mark{position:absolute;left:0;right:0;top:105px;text-align:center;font-size:26px;font-weight:700;color:var(--faint)}
  .sheet .wave{height:26px}
  .fax-title{position:absolute;left:10px;top:32px;font-size:7px;font-weight:700;color:var(--blue)}
  .fax-table{position:absolute;left:10px;top:44px;width:180px;border-collapse:collapse}
  .fax-table td{border:0.5px solid var(--rule);height:9px;font-size:4px;padding:0 3px;color:var(--ink)}
  .fax-table td.label{background:#8a9096;color:#fff;width:30px}

  /* small envelopes */
  .env-sm{left:700px;width:212px;height:90px}
  .env-sm.a{top:96px}
  .env-sm.b{top:192px;height:84px}
  .env-sm .brand{position:absolute;left:8px;top:8px;font-size:7px}
  .env-sm .brand .dot{width:6px;height:6px}
  .env-sm .ret{position:absolute;left:8px;top:18px}
  .env-sm .wave{height:14px}

  /* DL envelopes */
  .env-dl{left:960px;width:228px;height:70px}
  .env-dl.back-blue{top:70px}
  .env-dl.back-white{top:130px}
  .env-dl.front{top:194px}
  .env-dl svg.flap{position:absolute;left:0;top:0;width:100%;height:100%}
  .env-dl .flap-mark{position:absolute;left:0;right:0;top:12px;display:flex;justify-content:center}
  .env-dl .flap-mark .brand{font-size:7px}
  .env-dl .flap-mark .brand .dot{width:6px;height:6px}
  .env-dl.back-blue .brand{color:#fff}
  .env-dl.back-blue .brand .dot{background:#fff}
  .env-dl.front .brand{position:absolute;left:8px;top:8px;font-size:7px}
  .env-dl.front .brand .dot{width:6px;height:6px}
  .env-dl.front .ret{position:absolute;left:8px;top:18px}
  .env-dl.front .wave{height:10px}
</style>
</head>
<body>

<div class="logo-master">
  <div class="brand"><span class="dot"></span>Tessaline</div>
  <div class="sub">Products Design</div>
</div>

<div class="piece card-dark">
  <div class="brand"><span class="dot"></span>Tessaline</div>
  <svg class="wave" viewBox="0 0 120 14" preserveAspectRatio="none"><path d="M0 8 Q40 0 120 6 L120 14 L0 14Z" fill="var(--green)"/></svg>
</div>

<div class="piece card-front">
  <div class="brand"><span class="dot"></span>Tessaline</div>
  <div class="details tiny">
    <strong>Corin Maddox</strong><br>Founder, VP Operations<br>P.O. Box 4682<br>Wildomar, CA 92871<br>corin@tessalinegoods.example
  </div>
  <svg class="wave" viewBox="0 0 108 12" preserveAspectRatio="none"><path d="M0 6 Q40 0 108 5 L108 12 L0 12Z" fill="var(--blue)"/><path d="M0 9 Q50 3 108 8 L108 12 L0 12Z" fill="var(--green)"/></svg>
</div>

<div class="piece card-back">
  <div class="brand"><span class="dot"></span>Tessaline</div>
</div>

<div class="piece sheet letterhead">
  <div class="head"><div class="brand"><span class="dot"></span>Tessaline</div></div>
  <div class="contact tiny">P.O. Box 4682<br>Wildomar, CA 92871<br>www.tessalinegoods.example</div>
  <div class="mark">Tessaline</div>
  <svg class="wave" viewBox="0 0 200 26" preserveAspectRatio="none"><path d="M0 10 Q80 0 200 12 L200 26 L0 26Z" fill="var(--blue)"/><path d="M0 16 Q100 6 200 18 L200 26 L0 26Z" fill="var(--green)"/></svg>
</div>

<div class="piece sheet fax">
  <div class="head"><div class="brand"><span class="dot"></span>Tessaline</div></div>
  <div class="contact tiny">P.O. Box 4682<br>Wildomar, CA 92871<br>www.tessalinegoods.example</div>
  <div class="fax-title">FAX</div>
  <table class="fax-table">
    <tr><td class="label">To</td><td></td><td class="label">From</td><td></td></tr>
    <tr><td class="label">Fax</td><td></td><td class="label">Pages</td><td></td></tr>
    <tr><td class="label">Phone</td><td></td><td class="label">Date</td><td></td></tr>
    <tr><td class="label">Re</td><td colspan="3"></td></tr>
  </table>
  <div class="mark">Tessaline</div>
  <svg class="wave" viewBox="0 0 200 26" preserveAspectRatio="none"><path d="M0 10 Q80 0 200 12 L200 26 L0 26Z" fill="var(--blue)"/><path d="M0 16 Q100 6 200 18 L200 26 L0 26Z" fill="var(--green)"/></svg>
</div>

<div class="piece env-sm a">
  <div class="brand"><span class="dot"></span>Tessaline</div>
  <div class="ret tiny">P.O. Box 4682<br>Wildomar, CA 92871</div>
  <svg class="wave" viewBox="0 0 212 14" preserveAspectRatio="none"><path d="M0 6 Q90 0 212 6 L212 14 L0 14Z" fill="var(--blue)"/><path d="M0 10 Q100 4 212 9 L212 14 L0 14Z" fill="var(--green)"/></svg>
</div>

<div class="piece env-sm b">
  <div class="brand"><span class="dot"></span>Tessaline</div>
  <div class="ret tiny">P.O. Box 4682<br>Wildomar, CA 92871</div>
  <svg class="wave" viewBox="0 0 212 14" preserveAspectRatio="none"><path d="M0 6 Q90 0 212 6 L212 14 L0 14Z" fill="var(--blue)"/><path d="M0 10 Q100 4 212 9 L212 14 L0 14Z" fill="var(--green)"/></svg>
</div>

<div class="piece env-dl back-blue">
  <svg class="flap" viewBox="0 0 228 70" preserveAspectRatio="none"><path d="M0 0 L228 0 L228 20 L114 44 L0 20Z" fill="var(--blue)"/><path d="M0 70 L114 40 L228 70" fill="none" stroke="var(--rule)" stroke-width="0.6"/></svg>
  <div class="flap-mark"><div class="brand"><span class="dot"></span>Tessaline</div></div>
</div>

<div class="piece env-dl back-white">
  <svg class="flap" viewBox="0 0 228 70" preserveAspectRatio="none"><path d="M0 0 L114 44 L228 0" fill="none" stroke="var(--rule)" stroke-width="0.8"/><path d="M0 70 L114 40 L228 70" fill="none" stroke="var(--rule)" stroke-width="0.6"/></svg>
  <div class="flap-mark"><div class="brand"><span class="dot"></span>Tessaline</div></div>
</div>

<div class="piece env-dl front">
  <div class="brand"><span class="dot"></span>Tessaline</div>
  <div class="ret tiny">P.O. Box 4682<br>Wildomar, CA 92871</div>
  <svg class="wave" viewBox="0 0 228 10" preserveAspectRatio="none"><path d="M0 4 Q100 0 228 4 L228 10 L0 10Z" fill="var(--blue)"/><path d="M0 7 Q110 3 228 7 L228 10 L0 10Z" fill="var(--green)"/></svg>
</div>

</body>
</html>
```